Book Cover for College Series

We need an e-book cover design for a collection of poetry entitled, "Chalk Lanterns Vol. 1: The Heartland." Although the price is set to $200, whomever I select for this project will be used for the next three volumes of the series in the future. So be sure to have contact information ready if selected.
If selected, we can be reached at BrightQuillPress@mailnest.example
Be sure to check out the Look and Feel Slider. We would like it to come across as serious and professional, yet very personable and modern.
Target Market(s)
Target market is both current college students as well as former college students (University alums). However, on some level it is marketed towards anyone associated with universities, including professors, as well as poetry readers. Which is why, although personable, We need the look to have a serious feel to it as well.
Industry/Entity Type
College
Requirements
Must have
- The title of the book: "Chalk Lanterns: Vol 1. The Heartland"
- Be sure to have the author's name: Benedict Marlow Tesh
Nice to have
- - Nice to have a design that somehow gives off the feeling of nostalgia.
Optional: Underneath the title, include "A collection of poetry celebrating the top universities of the Midwest."
- Only include the following if it does not get in the way of the feel/look of the cover: Have the initials: B.M.T. on the left-hand corner. An example of how this should appear is in the photo attached However, it does not necessarily need to be this big.

```html
<!DOCTYPE html>
<html lang="en">
<head>
<meta charset="utf-8">
<title>Chalk Lanterns: Vol 1. The Heartland — Benedict Marlow Tesh</title>
<link rel="stylesheet" href="https://fonts.googleapis.com/css2?family=Crimson+Pro:ital,wght@0,300;1,300;1,400&family=Montserrat:wght@400&family=Oswald:wght@500&display=swap">
<style>
  :root {
    --page: #ffffff;
    --sky: #d3e6f2;
    --ink: #55585b;
    --ink-soft: #5d6063;
    --rule: #6a6d70;
    --field-gold: #d9a83a;
    --field-olive: #7b8148;
    --hill-grey: #9c968a;
    --ground: #cfc4b1;
    --initials: #ffffff;
  }
  * { box-sizing: border-box; margin: 0; padding: 0; }
  html, body {
    width: 849px;
    height: 1200px;
    overflow: hidden;
    background: var(--page);
  }
  .stage {
    width: 849px;
    height: 1200px;
    display: flex;
    align-items: center;
    justify-content: center;
  }
  .cover {
    position: relative;
    width: 793px;
    height: 1160px;
    background: var(--sky);
    overflow: hidden;
  }
  .cover__tagline {
    position: absolute;
    left: 51px;
    top: 56px;
    width: 300px;
    font-family: "Montserrat", Arial, sans-serif;
    font-size: 18px;
    line-height: 1.45;
    color: var(--ink-soft);
  }
  .cover__title {
    position: absolute;
    left: 49px;
    top: 166px;
    font-family: "Crimson Pro", Georgia, serif;
    font-weight: 300;
    font-size: 56px;
    line-height: 1.08;
    color: var(--ink);
  }
  .cover__rule {
    position: absolute;
    left: 51px;
    top: 318px;
    width: 88px;
    height: 2px;
    background: var(--rule);
  }
  .cover__author {
    position: absolute;
    left: 49px;
    top: 340px;
    font-family: "Crimson Pro", Georgia, serif;
    font-style: italic;
    font-weight: 400;
    font-size: 52px;
    color: var(--ink);
  }
  .cover__landscape {
    position: absolute;
    left: 0;
    right: 0;
    bottom: 0;
    height: 330px;
    background: linear-gradient(
      to bottom,
      var(--sky) 0%,
      var(--hill-grey) 10%,
      var(--field-olive) 22%,
      var(--field-gold) 40%,
      var(--hill-grey) 58%,
      var(--ground) 72%,
      var(--ground) 100%
    );
  }
  .cover__initials {
    position: absolute;
    left: 51px;
    bottom: 48px;
    font-family: "Oswald", Arial, sans-serif;
    font-weight: 500;
    font-size: 42px;
    letter-spacing: 1px;
    color: var(--initials);
  }
</style>
</head>
<body>
  <main class="stage">
    <section class="cover">
      <p class="cover__tagline">A collection of poetry celebrating the top universities of the Midwest.</p>
      <h1 class="cover__title">Chalk Lanterns<br>Vol 1. The Heartland</h1>
      <div class="cover__rule"></div>
      <p class="cover__author">Benedict Marlow Tesh</p>
      <div class="cover__landscape" role="img" aria-label="Flat illustration of rolling Midwest hills with golden fields, trees and a small red-roofed farm"></div>
      <p class="cover__initials">BMT</p>
    </section>
  </main>
</body>
</html>
```